依頼詳細
残暑お見舞い申し上げます

コロナ禍と暑さで汗が噴き出るような日々が続きますが、いかがお過ごしでしょうか?
汗はかけばかくほど、老廃物が体内から出て、心も体も健康になります。
汗をかかないようにすることは、決して良いことではありません。
会社にとっても、今年は汗(特別損失)を出せるチャンスです。
個人も会社もたくさんの汗を出して、より健康体になられること、心より祈念申し上げます。

★写真に添える文章:松本清志の最新刊
「伸びる会社へ組み直す」
定価10,780円(税込み)
記載項目
ノルフェン・パートナーズ
松本 清志・長谷 宗一郎・柴田 昌平
希望イメージ
シンプル 複雑
単色 カラフル
暗い 明るい
日常 高級
遊び心 厳粛
未来的 伝統的
女性的 男性的
希望する色
水色系
納品ファイル
• 高解像度JPG (.jpg)
補足説明
■ 選んだ理由

今年はコロナのイベント中止で花火大会もなくなるなかで、
もってこいのデザインでした。
文字の並べ方に工夫が見られ、メッセージとバックのコントラストが素敵でした。
一目見ておしゃれで気に入りました。

■ 提案者全員のお礼・コメント

この度は、ご応募ありがとうございました。
毎回、新たなご提案が来るのが楽しみでした。素敵なご応募をありがとうございました。

```html
<!DOCTYPE html>
<html lang="ja">
<head>
<meta charset="UTF-8">
<title>残暑お見舞い</title>
<link href="https://fonts.googleapis.com/css2?family=Noto+Serif+JP:wght@500;700&family=Noto+Sans+JP:wght@500&display=swap" rel="stylesheet">
<style>
  :root {
    --water-deep: #0a4f8c;
    --water-mid: #1e86c4;
    --water-light: #5cc3ec;
    --band: #1f8ea3;
    --ink-light: #ffffff;
    --ink-accent: #dff6ff;
    --book-red: #9a2a20;
    --book-dark: #4a1410;
  }
  * { margin: 0; padding: 0; box-sizing: border-box; }
  html, body { width: 810px; height: 1200px; overflow: hidden; }
  .card {
    position: relative;
    width: 810px;
    height: 1200px;
    overflow: hidden;
    font-family: "Noto Serif JP", serif;
    color: var(--ink-light);
  }
  .water {
    position: absolute;
    inset: 0 0 130px 0;
    background:
      radial-gradient(ellipse at 30% 20%, var(--water-light) 0%, transparent 55%),
      radial-gradient(ellipse at 75% 60%, var(--water-light) 0%, transparent 50%),
      linear-gradient(170deg, var(--water-mid) 0%, var(--water-deep) 60%, var(--water-mid) 100%);
  }
  .greeting {
    position: absolute;
    top: 48px;
    left: 0;
    width: 100%;
    text-align: center;
    font-size: 40px;
    font-weight: 700;
    letter-spacing: 0.08em;
    text-shadow: 0 2px 6px rgba(0, 30, 70, 0.5);
  }
  .message {
    position: absolute;
    top: 210px;
    left: 0;
    width: 100%;
    text-align: center;
    font-size: 24px;
    font-weight: 500;
    line-height: 44px;
    text-shadow: 0 1px 4px rgba(0, 30, 70, 0.6);
  }
  .message .gap { display: block; height: 10px; }
  .sender {
    position: absolute;
    top: 660px;
    left: 0;
    width: 100%;
    text-align: center;
    color: var(--ink-accent);
    text-shadow: 0 1px 4px rgba(0, 30, 70, 0.6);
  }
  .sender .company { font-size: 30px; font-weight: 700; letter-spacing: 0.06em; }
  .sender .names { font-size: 24px; font-weight: 500; margin-top: 6px; letter-spacing: 0.04em; }
  .book-photo {
    position: absolute;
    left: 448px;
    top: 770px;
    width: 330px;
    height: 390px;
    background: linear-gradient(120deg, var(--book-red) 0%, var(--book-dark) 100%);
    box-shadow: 0 8px 20px rgba(0, 0, 0, 0.35);
    z-index: 2;
  }
  .book-band {
    position: absolute;
    left: 0;
    bottom: 0;
    width: 100%;
    height: 130px;
    background: var(--band);
  }
  .book-caption {
    position: absolute;
    left: 32px;
    top: 18px;
    font-family: "Noto Sans JP", sans-serif;
    font-weight: 500;
    font-size: 25px;
    line-height: 33px;
  }
</style>
</head>
<body>
<div class="card">
  <div class="water" role="img" aria-label="きらめくプールの水面の写真"></div>

  <h1 class="greeting">残暑お見舞い申し上げます</h1>

  <p class="message">
    コロナ禍と暑さで汗が噴き出るような日々が続きますが、<br>
    いかがお過ごしでしょうか?<br>
    汗はかけばかくほど、老廃物が体内から出て、<br>
    心も体も健康になります。<span class="gap"></span>
    汗をかかないようにすることは、決して良いことではありません。<br>
    会社にとっても、今年は汗(特別損失)を出せるチャンスです。<br>
    個人も会社もたくさんの汗を出して、より健康体になられること、<br>
    心より祈念申し上げます。
  </p>

  <div class="sender">
    <p class="company">ノルフェン・パートナーズ</p>
    <p class="names">松本　清志・長谷　宗一郎・柴田　昌平</p>
  </div>

  <div class="book-band">
    <p class="book-caption">
      松本清志の最新刊<br>
      「伸びる会社へ組み直す」<br>
      定価10,780円(税込)
    </p>
  </div>

  <div class="book-photo" role="img" aria-label="新刊『伸びる会社へ組み直す』の書籍写真"></div>
</div>
</body>
</html>
```